Need sign/billboard help

I need somone to take my logo and turn it into a sign.
Needs to have: Bright Paws
Hound Play Lodge LLC
319-555-0187
Daycare - Boarding - Learning
Colors to use are in the pictures i included, however feel free to use different shades of gray. i Don't necessary want to background to be one solid color.
Also this sing will be a rectangle (4'x8')
Industry/Entity Type
Daycare
Look and feel
Each slider illustrates characteristics of the customer's brand and the style your logo design should communicate.

```html
<!DOCTYPE html>
<html lang="en">
<head>
<meta charset="utf-8">
<title>Hound Play Lodge LLC — Sign</title>
<link rel="stylesheet" href="https://fonts.googleapis.com/css2?family=Bebas+Neue&display=swap">
<style>
  :root {
    --lime: #b4c800;
    --lime-light: #c9d84a;
    --lime-pale: #d3df7a;
    --lime-bright: #e8f000;
    --olive: #7f9000;
    --olive-deep: #4b5a14;
    --ink: #111111;
    --white: #ffffff;
    --shadow: #3a3a2a;
  }
  * { margin: 0; padding: 0; box-sizing: border-box; }
  html, body {
    width: 1200px;
    height: 849px;
    overflow: hidden;
    background: var(--lime);
  }
  .sign {
    position: relative;
    width: 1200px;
    height: 849px;
    overflow: hidden;
    background: var(--lime);
    font-family: "Bebas Neue", "Oswald", sans-serif;
  }
  .streak {
    position: absolute;
    left: 0;
    width: 1200px;
  }
  .streak--pale   { top: 248px; height: 62px; background: linear-gradient(90deg, transparent 0%, var(--lime-pale) 20%, var(--lime-pale) 75%, transparent 100%); opacity: .55; }
  .streak--dark   { top: 320px; height: 26px; background: linear-gradient(90deg, var(--olive) 0%, var(--olive) 40%, transparent 95%); opacity: .55; }
  .streak--bright { top: 368px; height: 44px; background: linear-gradient(90deg, var(--lime-bright) 0%, var(--lime-bright) 55%, transparent 100%); opacity: .8; }
  .streak--thin   { top: 436px; height: 8px;  background: linear-gradient(90deg, transparent 40%, var(--lime-bright) 60%, var(--lime-bright) 100%); }
  .streak--soft   { top: 492px; height: 50px; background: linear-gradient(90deg, var(--lime-light) 0%, transparent 70%); opacity: .6; }
  .streak--low    { top: 690px; height: 56px; background: linear-gradient(90deg, transparent 0%, var(--olive) 15%, var(--olive) 60%, transparent 100%); opacity: .45; }
  .streak--base   { top: 770px; height: 22px; background: linear-gradient(90deg, var(--lime-light) 0%, transparent 60%); opacity: .6; }

  .company-name {
    position: absolute;
    top: 40px;
    left: 0;
    width: 1200px;
    text-align: center;
    font-size: 104px;
    line-height: 1;
    color: var(--olive-deep);
    letter-spacing: 1px;
  }
  .brand {
    position: absolute;
    top: 360px;
    left: 0;
    width: 1200px;
    display: flex;
    justify-content: center;
    align-items: center;
    gap: 28px;
  }
  .brand__mark {
    width: 70px;
    height: 70px;
    border-radius: 50%;
    background: var(--ink);
  }
  .brand__name {
    font-size: 140px;
    line-height: 1;
    color: var(--ink);
    letter-spacing: 3px;
  }
  .services {
    position: absolute;
    top: 585px;
    left: 0;
    width: 1200px;
    text-align: center;
    font-size: 62px;
    line-height: 1;
    color: var(--olive-deep);
    letter-spacing: 1px;
    word-spacing: 10px;
  }
  .phone {
    position: absolute;
    top: 655px;
    left: 0;
    width: 1200px;
    text-align: center;
    font-size: 168px;
    line-height: 1;
    color: var(--white);
    letter-spacing: 2px;
    text-shadow: 6px 6px 0 var(--shadow);
  }
</style>
</head>
<body>
  <main class="sign">
    <div class="streak streak--pale"></div>
    <div class="streak streak--dark"></div>
    <div class="streak streak--bright"></div>
    <div class="streak streak--thin"></div>
    <div class="streak streak--soft"></div>
    <div class="streak streak--low"></div>
    <div class="streak streak--base"></div>

    <h1 class="company-name">Hound Play Lodge LLC</h1>

    <div class="brand">
      <span class="brand__mark"></span>
      <span class="brand__name">BRIGHT PAWS</span>
    </div>

    <p class="services">DAYCARE | BOARDING | LEARNING</p>
    <p class="phone">319-555-0187</p>
  </main>
</body>
</html>
```